macro advisory firm intro powerpoint

I have the bones of an introductory deck for a new firm. Need to make it much more professionally designed. Want it to also be customizable when received so I can adjust wording, etc. use colors similar to typical finance firm. high end fonts, etc.

```html
<!DOCTYPE html>
<html lang="en">
<head>
<meta charset="utf-8">
<title>Meridian Crest – Introductory Deck</title>
<link href="https://fonts.googleapis.com/css2?family=Montserrat:wght@400;500;600;700;800&display=swap" rel="stylesheet">
<style>
:root{
  --board:#7b8180;
  --sand:#e1d6c1;
  --sand-light:#ece4d4;
  --sand-dark:#cfc2a9;
  --ink:#1d2023;
  --ink-soft:#3a3d40;
  --muted:#6f6758;
  --red:#d63f26;
  --white:#ffffff;
  --card:rgba(255,255,255,.32);
}
*{box-sizing:border-box;margin:0;padding:0}
html,body{width:1075px;height:1200px;overflow:hidden;background:var(--board);font-family:'Montserrat',sans-serif;color:var(--ink)}
.board{position:relative;width:1075px;height:1200px}
.slide{position:absolute;width:760px;height:427px;transform:scale(.5906);transform-origin:0 0;overflow:hidden;
  background:radial-gradient(ellipse at 30% 40%,var(--sand-light),var(--sand) 55%,var(--sand-dark));
  box-shadow:0 14px 30px rgba(0,0,0,.35)}
.s1{left:83px;top:73px}.s2{left:543px;top:73px}
.s3{left:83px;top:340px}.s4{left:543px;top:340px}
.s5{left:83px;top:607px}.s6{left:543px;top:607px}
.s7{left:83px;top:874px}.s8{left:543px;top:874px}
.abs{position:absolute}

/* brand lockup */
.brand{position:absolute;display:flex;align-items:flex-start;gap:6px}
.brand .mark{width:26px;height:26px;background:var(--ink);margin-top:2px;flex:none}
.brand .name{font-weight:700;font-size:13px;line-height:1.05;letter-spacing:.5px;color:var(--ink);width:72px}
.brand .tag{font-weight:600;font-size:5px;line-height:1.35;letter-spacing:.3px;margin-top:3px;border-top:1px solid var(--ink);padding-top:2px;color:var(--ink)}
.brand.light .mark{background:var(--white)}
.brand.light .name,.brand.light .tag{color:var(--white);border-color:var(--white)}
.brand.hero .mark{width:70px;height:80px}
.brand.hero{gap:10px}
.brand.hero .name{font-size:30px;width:150px}
.brand.hero .tag{font-size:10px;margin-top:8px;padding-top:5px}
.brand.mid .mark{width:48px;height:56px}
.brand.mid .name{font-size:21px;width:105px}
.brand.mid .tag{font-size:7.5px}

.header{position:absolute;left:31px;top:25px;background:var(--ink);color:var(--white);font-weight:500;font-size:27px;padding:0 24px;height:51px;display:flex;align-items:center;line-height:1.1}
.subhead{position:absolute;font-size:18px;font-weight:500;color:var(--ink)}
.page{position:absolute;left:728px;top:398px;width:18px;height:18px;background:var(--ink);transform:rotate(45deg)}
.page span{display:block;transform:rotate(-45deg);color:var(--white);font-size:4.5px;text-align:center;line-height:18px;font-weight:700}

.dia{position:absolute;width:40px;height:40px;transform:rotate(45deg);display:flex;align-items:center;justify-content:center;box-shadow:0 2px 5px rgba(0,0,0,.25)}
.dia.w{background:var(--white);border:2px solid var(--ink)}
.dia.r{background:var(--red);border:2px solid var(--ink)}
.dia.k{background:var(--ink)}
.dia svg{transform:rotate(-45deg);width:16px;height:16px}
.item-title{position:absolute;font-weight:800;font-size:13px;line-height:1.4;color:var(--ink)}
.item-text{position:absolute;font-size:11.5px;line-height:1.7;color:var(--muted)}
.item-text.sm{font-size:9.5px;line-height:1.55}

.photo{position:absolute}
.red-band{position:absolute;background:var(--red);color:var(--white);font-weight:500;display:flex;align-items:center;justify-content:center}

/* about cards */
.card-title{position:absolute;font-weight:800;font-size:12.5px;text-align:center;width:209px}
.card-text{position:absolute;font-size:10.8px;line-height:1.6;text-align:center;width:190px}

.bio-card{position:absolute;width:170px;height:153px;background:var(--card);border-radius:4px}
.bio-card h4{position:absolute;left:20px;top:40px;font-weight:600;font-size:10.5px;line-height:1.6}
.bio-card p{position:absolute;left:20px;font-size:8.6px;line-height:1.7;color:var(--ink-soft);width:140px}
</style>
</head>
<body>
<div class="board">

<!-- 1 Title -->
<section class="slide s1">
  <div class="brand hero" style="left:240px;top:72px">
    <span class="mark"></span>
    <div><div class="name">MERIDIAN CREST</div><div class="tag">GEOPOLITICAL<br>ECONOMIC · POLICY<br>ANALYSIS</div></div>
  </div>
  <div class="red-band" style="left:104px;top:231px;width:552px;height:74px;font-size:46px">Presentation Title</div>
  <div class="abs" style="left:0;width:760px;top:325px;text-align:center;font-size:17px">September 22,2025</div>
</section>

<!-- 2 Why Clients -->
<section class="slide s2">
  <div class="header" style="width:385px">Why Clients Seek Us</div>
  <div class="brand" style="left:622px;top:28px"><span class="mark"></span><div><div class="name">MERIDIAN CREST</div><div class="tag">GEOPOLITICAL<br>ECONOMIC · POLICY<br>ANALYSIS</div></div></div>
  <div class="subhead" style="left:52px;top:100px">Credibility | Access | Results</div>

  <div class="dia w" style="left:46px;top:180px"><svg viewBox="0 0 16 16"><path d="M2 6h12L8 2zM3 7h2v6H3zM7 7h2v6H7zM11 7h2v6h-2zM2 13h12v1.5H2z" fill="#1d2023"/></svg></div>
  <div class="item-title" style="left:113px;top:163px">INSTITUTIONAL TRUST</div>
  <div class="item-text" style="left:113px;top:190px">Experience at Senior Levels in<br>Private and Public Sector</div>

  <div class="dia r" style="left:403px;top:180px"><svg viewBox="0 0 16 16"><path d="M8 2l5 3v6l-5 3-5-3V5z" fill="#fff"/></svg></div>
  <div class="item-title" style="left:470px;top:163px">ANALYTIC RIGOR</div>
  <div class="item-text" style="left:470px;top:190px">Advanced Modeling &amp;<br>Proprietary Scenario Frameworks</div>

  <div class="dia r" style="left:46px;top:288px"><svg viewBox="0 0 16 16"><rect x="6" y="2" width="4" height="4" fill="#fff"/><rect x="1.5" y="10" width="4" height="4" fill="#fff"/><rect x="6" y="10" width="4" height="4" fill="#fff"/><rect x="10.5" y="10" width="4" height="4" fill="#fff"/><path d="M8 6v4M3.5 10V8h9v2" stroke="#fff" fill="none"/></svg></div>
  <div class="item-title" style="left:113px;top:271px">NETWORK ADVANTAGE</div>
  <div class="item-text" style="left:113px;top:298px">Deep Relationships with Policymakers<br>and Regulators</div>

  <div class="dia w" style="left:403px;top:288px"><svg viewBox="0 0 16 16"><path d="M3 13l1-3 7-7 2 2-7 7z" fill="#1d2023"/></svg></div>
  <div class="item-title" style="left:470px;top:271px">OUTCOME FOCUSED</div>
  <div class="item-text" style="left:470px;top:298px">Insight built to drive<br>decisions—not just commentary</div>
  <div class="page"><span>05</span></div>
</section>

<!-- 3 About Us -->
<section class="slide s3">
  <div class="header" style="width:187px;height:48px">About Us</div>
  <div class="abs" style="left:240px;top:26px;font-size:12.3px;line-height:1.65">Our goal is to provide strategic and actionable insight<br>today, so our clients are prepared for tomorrow</div>
  <div class="brand" style="left:622px;top:28px"><span class="mark"></span><div><div class="name">MERIDIAN CREST</div><div class="tag">GEOPOLITICAL<br>ECONOMIC · POLICY<br>ANALYSIS</div></div></div>

  <svg class="abs" style="left:0;top:0" width="760" height="427">
    <polygon points="57,216 266,216 266,355 161,398 57,355" fill="#fff"/>
    <polygon points="280,216 489,216 489,355 384,398 280,355" fill="#d63f26"/>
    <polygon points="502,216 711,216 711,355 606,398 502,355" fill="#fff"/>
  </svg>
  <div class="photo" role="img" aria-label="Close-up of a hand moving a chess piece" style="left:57px;top:108px;width:209px;height:108px;background:linear-gradient(135deg,#3a2a1e,#120c08 60%,#6b5238)"></div>
  <div class="photo" role="img" aria-label="The word strategy with an upward arrow on a grey wall" style="left:280px;top:108px;width:209px;height:108px;background:linear-gradient(90deg,#8e9294,#c7c9c8 35%,#b9bbbb)"></div>
  <div class="photo" role="img" aria-label="Hand placing a piece on a strategy board game" style="left:502px;top:108px;width:209px;height:108px;background:linear-gradient(135deg,#8a6a3c,#4f5a36 55%,#b48a4e)"></div>

  <div class="card-title" style="left:57px;top:240px">WHO WE SERVE</div>
  <div class="card-text" style="left:67px;top:262px">C-Suite executives,<br>Financial Institutions , Hedge Funds,Sovereign Wealth Funds, Family Offices</div>
  <div class="card-title" style="left:280px;top:240px;color:#fff">WHAT WE DO</div>
  <div class="card-text" style="left:290px;top:262px;color:#f6d6ce">Decode U.S. Public Policy Trends Thru a Sophisticated Lens of Economics, Geopolitical Analysis and Deep Relationships</div>
  <div class="card-title" style="left:502px;top:240px">OUR TEAM</div>
  <div class="card-text" style="left:512px;top:262px">Former Federal and State Government Advisors who are Economists, Academics and Practitioners</div>
  <div class="page"><span>02</span></div>
</section>

<!-- 4 Co-Founder -->
<section class="slide s4">
  <div class="header" style="width:250px">Co-Founder</div>
  <div class="abs" style="left:305px;top:24px;font-size:21px;line-height:1.4;font-weight:500">Daniel Arlen-Brooks,<br>Ph.D, MBA</div>
  <div class="brand" style="left:622px;top:28px"><span class="mark"></span><div><div class="name">MERIDIAN CREST</div><div class="tag">GEOPOLITICAL<br>ECONOMIC · POLICY<br>ANALYSIS</div></div></div>
  <div class="abs" style="left:548px;top:78px;width:78px;height:78px;transform:rotate(45deg);border:2px solid var(--ink)"></div>
  <div class="photo" role="img" aria-label="Portrait of the co-founder in a suit" style="left:540px;top:68px;width:78px;height:78px;transform:rotate(45deg);background:linear-gradient(135deg,#4d4a48,#1e2228);"></div>
  <div class="abs" style="left:52px;top:100px;font-size:12.2px;line-height:1.75">Economic Strategist | Author |Captain U.S. Army<br>Reserve (SME Finance &amp; Banking) | Deputy Chief of<br>Staff, Governor Thomas Wexley</div>

  <div class="bio-card" style="left:31px;top:195px"><h4>Government &amp;<br>Budget Leadership</h4><p style="top:85px">$87B+ oversight, economic competitiveness strategy for Virginia</p></div>
  <div class="bio-card" style="left:207px;top:230px"><h4>Defense Sector<br>Expertise</h4><p style="top:83px;text-align:center">Captain, U.S. Army Reserve – Civil Affairs, Financial Specialization</p></div>
  <div class="bio-card" style="left:384px;top:195px"><h4 style="top:44px">Cross-Sector Executive</h4><p style="top:66px;width:120px">Northfield Holdings (Investments), Macro Policy Advisors (Consulting)</p></div>
  <div class="bio-card" style="left:560px;top:230px"><h4 style="top:40px">Thought Leadership</h4><p style="top:66px;width:140px">Author, policy lecturer, media contributor (Market Wire, Ledger,Civic Radio)</p></div>

  <div class="dia k" style="left:96px;top:175px"><svg viewBox="0 0 16 16"><rect x="4" y="2" width="8" height="12" fill="#fff"/><rect x="6" y="4" width="1.5" height="1.5"/><rect x="8.5" y="4" width="1.5" height="1.5"/><rect x="6" y="7" width="1.5" height="1.5"/><rect x="8.5" y="7" width="1.5" height="1.5"/></svg></div>
  <div class="dia r" style="left:272px;top:210px"><svg viewBox="0 0 16 16"><path d="M2 14V6l4 3V6l4 3V3h4v11z" fill="#fff"/></svg></div>
  <div class="dia k" style="left:449px;top:175px"><svg viewBox="0 0 16 16"><rect x="2" y="3" width="12" height="8" fill="none" stroke="#fff" stroke-width="1.5"/><path d="M6 13h4" stroke="#fff" stroke-width="1.5"/></svg></div>
  <div class="dia r" style="left:625px;top:210px"><svg viewBox="0 0 16 16"><circle cx="8" cy="5" r="3" fill="#fff"/><path d="M2.5 14c0-3.5 2.5-5 5.5-5s5.5 1.5 5.5 5z" fill="#fff"/></svg></div>
  <div class="page"><span>06</span></div>
</section>

<!-- 5 Strategic Advisory -->
<section class="slide s5">
  <div class="header" style="width:429px;height:75px;font-size:26px">A Strategic Advisory for an<br>Evolving Environment</div>
  <div class="brand" style="left:622px;top:28px"><span class="mark"></span><div><div class="name">MERIDIAN CREST</div><div class="tag">GEOPOLITICAL<br>ECONOMIC · POLICY<br>ANALYSIS</div></div></div>
  <div class="subhead" style="left:52px;top:125px;font-size:16px">Introduction – Meridian Crest Macro Advisory</div>

  <div class="dia w" style="left:43px;top:186px"><svg viewBox="0 0 16 16"><circle cx="8" cy="8" r="6" fill="none" stroke="#1d2023" stroke-width="1.5"/><circle cx="8" cy="8" r="3" fill="none" stroke="#1d2023" stroke-width="1.5"/><circle cx="8" cy="8" r="1" fill="#1d2023"/></svg></div>
  <div class="item-title" style="left:105px;top:182px">SPECIALIZED<br>FOCUS</div>
  <div class="item-text sm" style="left:105px;top:222px;width:125px">US policy – Defense and Defense Tech, Government Relation Strategy, Manufacturing, Tax, Trade, International Relations, acroeconomic strategy.</div>

  <div class="dia r" style="left:264px;top:186px"><svg viewBox="0 0 16 16"><circle cx="8" cy="8" r="4" fill="#fff"/><circle cx="8" cy="8" r="1.5" fill="#d63f26"/></svg></div>
  <div class="item-title" style="left:327px;top:182px">OPERATIONAL<br>EXPERTISE</div>
  <div class="item-text sm" style="left:327px;top:222px;width:125px">Multi-Billion Dollar Budgets, Public-Private Investment Design, Government Relations Implementation</div>

  <div class="dia w" style="left:264px;top:326px"><svg viewBox="0 0 16 16"><circle cx="8" cy="5" r="2.3" fill="#1d2023"/><circle cx="3.5" cy="6.5" r="1.8" fill="#1d2023"/><circle cx="12.5" cy="6.5" r="1.8" fill="#1d2023"/><path d="M4 13c0-3 2-4 4-4s4 1 4 4zM0.5 12c0-2 1.3-3 3-3l-0.5 3zM15.5 12c0-2-1.3-3-3-3l.5 3z" fill="#1d2023"/></svg></div>
  <div class="item-title" style="left:327px;top:322px">CLIENT IMPACT</div>
  <div class="item-text sm" style="left:327px;top:345px;width:125px">Actionable Guidance for Csuites and institutional investors</div>

  <div class="abs" style="left:525px;top:160px;width:170px;height:170px;transform:rotate(45deg);border:2px solid var(--ink)"></div>
  <div class="photo" role="img" aria-label="Abstract network of tangled dark lines on a light background" style="left:516px;top:140px;width:170px;height:170px;transform:rotate(45deg);background:radial-gradient(circle,#c7ccd1,#8d959c);border:4px solid var(--sand-light)"></div>
  <div class="page"><span>03</span></div>
</section>

<!-- 6 Advisory Services -->
<section class="slide s6">
  <div class="header" style="width:345px">Advisory Services</div>
  <div class="brand" style="left:622px;top:28px"><span class="mark"></span><div><div class="name">MERIDIAN CREST</div><div class="tag">GEOPOLITICAL<br>ECONOMIC · POLICY<br>ANALYSIS</div></div></div>
  <div class="subhead" style="left:52px;top:92px;font-size:16px">Flexible Models for Strategic Insight &amp; Engagement</div>

  <div class="abs" style="left:302px;top:188px;width:158px;height:158px;transform:rotate(45deg);border:2px solid var(--ink)"></div>
  <div class="photo" role="img" aria-label="Dark trading screen with candlestick chart and rising arrow" style="left:296px;top:175px;width:158px;height:158px;transform:rotate(45deg);background:linear-gradient(135deg,#0f1a22,#1d3542 55%,#0a1218);"></div>

  <div class="dia w" style="left:64px;top:172px"><svg viewBox="0 0 16 16"><path d="M4 9l3-6 2 1-1 3 4-1 1 3-4 4H5z" fill="#1d2023"/></svg></div>
  <div class="item-title" style="left:123px;top:168px">RETAINER ADVISORY</div>
  <div class="item-text sm" style="left:123px;top:192px;width:130px">Access to Senior Advisors, Regular Updates, Strategic counsel</div>

  <div class="dia r" style="left:64px;top:298px"><svg viewBox="0 0 16 16"><rect x="4" y="2" width="8" height="12" rx="1" fill="#fff"/><path d="M5 11h6" stroke="#d63f26"/></svg></div>
  <div class="item-title" style="left:123px;top:282px">PROJECT-BASED<br>ENGAGEMENTS</div>
  <div class="item-text sm" style="left:123px;top:322px;width:130px">In-depth, Bespoke Studies with Actionable Recommendations</div>

  <div class="dia r" style="left:506px;top:172px"><svg viewBox="0 0 16 16"><rect x="2" y="3" width="12" height="10" fill="none" stroke="#fff" stroke-width="1.5"/><path d="M2 7h12M2 10h12M6 3v10M10 3v10" stroke="#fff"/></svg></div>
  <div class="item-title" style="left:566px;top:155px">MARKET ENTRY &amp;<br>DUE DILIGENCE</div>
  <div class="item-text sm" style="left:566px;top:195px;width:150px">FullSpectrum Support for Cross-Border and Regulatory Risk, Strategic Introductions</div>

  <div class="dia w" style="left:506px;top:298px"><svg viewBox="0 0 16 16"><circle cx="8" cy="5" r="2.3" fill="#1d2023"/><circle cx="3.5" cy="6.5" r="1.8" fill="#1d2023"/><circle cx="12.5" cy="6.5" r="1.8" fill="#1d2023"/><path d="M4 13c0-3 2-4 4-4s4 1 4 4z" fill="#1d2023"/></svg></div>
  <div class="item-title" style="left:566px;top:290px">SPEAKERS</div>
  <div class="item-text sm" style="left:566px;top:313px;width:150px">Speakers for Board Meetings, Client Conferences, Curate Panels</div>
  <div class="page"><span>07</span></div>
</section>

<!-- 7 Section Divider -->
<section class="slide s7">
  <div class="photo" role="img" aria-label="Three colleagues collaborating at a laptop in a bright city office" style="left:0;top:0;width:760px;height:427px;background:linear-gradient(100deg,#e3d8c2 0%,#c9c2b2 30%,#6f8a8c 50%,#5a6e73 70%,#b9b3a3 100%)"></div>
  <div class="brand mid" style="left:75px;top:55px"><span class="mark"></span><div><div class="name">MERIDIAN CREST</div><div class="tag">GEOPOLITICAL<br>ECONOMIC · POLICY<br>ANALYSIS</div></div></div>
  <div class="red-band" style="left:220px;top:330px;width:540px;height:75px;font-size:38px">Section Divider Title</div>
</section>

<!-- 8 Thank You -->
<section class="slide s8">
  <div class="photo" role="img" aria-label="Blue-toned team meeting in a modern office" style="left:0;top:0;width:760px;height:427px;background:linear-gradient(110deg,#3c4b5c,#6f8093 45%,#4a5a6b 75%,#2d3945)"></div>
  <div class="brand light" style="left:632px;top:25px"><span class="mark"></span><div><div class="name">MERIDIAN CREST</div><div class="tag">GEOPOLITICAL<br>ECONOMIC · POLICY<br>ANALYSIS</div></div></div>
  <div class="red-band" style="left:376px;top:305px;width:384px;height:88px;font-size:52px">Thank You</div>
</section>

</div>
</body>
</html>
```